Toravelle Works Luxury Candles

Luxury box design,, simple and sophisticated look,,

My collection of candles come in 5 different fragrances, i would like to be able to change the fragrance name on the boxes,,,,

I would like the outline of australia on the front down the bottom , (only small) to represent this is an australian product.

My boxes are white gloss,,,

Happy for you to use my current logo ,,, however you'll have to change Toravelle Nails to Toravelle Works.

```html
<!DOCTYPE html>
<html lang="en">
<head>
<meta charset="utf-8">
<title>Toravelle Works Luxury Candles – Box Front</title>
<link rel="stylesheet" href="https://fonts.googleapis.com/css2?family=Cormorant+Garamond:wght@500&family=Cinzel:wght@400&display=swap">
<style>
  :root {
    --backdrop: #e9ebf1;
    --box-white: #ffffff;
    --box-edge: #dcdfe6;
    --ink: #1d1d22;
    --band-line: #d6d6da;
    --band-fill: #f6f6f7;
    --foil-rose: #b98f86;
    --foil-blush: #e6d3cf;
    --foil-silver: #c9cdd6;
    --foil-steel: #6f7b93;
    --foil-white: #fbfbfc;
    --map-tone: #e4e5e9;
  }
  * { box-sizing: border-box; margin: 0; padding: 0; }
  html, body {
    width: 960px;
    height: 1200px;
    overflow: hidden;
    background: var(--backdrop);
  }
  .canvas {
    position: relative;
    width: 960px;
    height: 1200px;
  }
  .box-front {
    position: absolute;
    left: 150px;
    top: 70px;
    width: 660px;
    height: 1060px;
    background: var(--box-white);
    border: 1px solid var(--box-edge);
    box-shadow: 0 18px 40px rgba(30, 34, 60, 0.12);
  }
  .brand-band {
    position: absolute;
    left: 40px;
    top: 250px;
    width: 580px;
    height: 84px;
    background:
      repeating-linear-gradient(to bottom, transparent 0 5px, var(--band-line) 5px 6px),
      var(--band-fill);
    display: flex;
    align-items: center;
    justify-content: center;
  }
  .brand-name {
    font-family: "Cormorant Garamond", serif;
    font-weight: 500;
    font-size: 40px;
    letter-spacing: 1px;
    color: var(--ink);
    background: var(--band-fill);
    padding: 0 18px;
  }
  .foil-panel {
    position: absolute;
    left: 40px;
    top: 334px;
    width: 580px;
    height: 580px;
    background:
      radial-gradient(ellipse 45% 40% at 88% 8%, var(--foil-rose) 0%, transparent 70%),
      radial-gradient(ellipse 55% 45% at 70% 25%, var(--foil-blush) 0%, transparent 75%),
      radial-gradient(ellipse 40% 30% at 5% 92%, var(--foil-steel) 0%, transparent 70%),
      radial-gradient(ellipse 60% 50% at 45% 80%, var(--foil-silver) 0%, transparent 75%),
      var(--foil-white);
  }
  .fragrance-name {
    position: absolute;
    left: 0;
    right: 0;
    top: 232px;
    text-align: center;
    font-family: "Cinzel", serif;
    font-weight: 400;
    font-size: 34px;
    letter-spacing: 1px;
    color: var(--ink);
  }
  .origin-map {
    position: absolute;
    left: 290px;
    top: 940px;
    width: 80px;
    height: 76px;
    background: var(--map-tone);
    border-radius: 6px;
  }
</style>
</head>
<body>
  <main class="canvas">
    <section class="box-front">
      <div class="brand-band">
        <span class="brand-name">Toravelle Works</span>
      </div>
      <div class="foil-panel" role="img" aria-label="Textured rose-gold and silver foil panel">
        <p class="fragrance-name">Vanilla Caramel</p>
      </div>
      <div class="origin-map" role="img" aria-label="Small outline map of Australia"></div>
    </section>
  </main>
</body>
</html>
```